New modern business card design

To design a brand new business card that's clean & modern in terms of layout.
I have attached our company logo and also basic information regarding what is needed on the card that also needs to be editable.

Target Market(s)

motor trade

Contact Information for Business Card

logo, name, title, tel, mob, email, address, www, all information is in the word.doc file

Requirements
Must have
• white background
Nice to have
• Nice clean font

```html
<!DOCTYPE html>
<html lang="en">
<head>
<meta charset="utf-8">
<title>Bolt Remove Ltd – Business Card</title>
<link rel="stylesheet" href="https://fonts.googleapis.com/css2?family=Open+Sans:wght@400;600;700&display=swap">
<style>
  :root {
    --page-bg: #d6d5d2;
    --card-bg: #ffffff;
    --card-edge: #c9c8c5;
    --brand-blue: #2f7fc8;
    --text-dark: #2a2b2f;
    --text-muted: #6e6f73;
    --rule: #3a3b3f;
  }
  * { margin: 0; padding: 0; box-sizing: border-box; }
  html, body {
    width: 1200px; height: 864px; overflow: hidden;
    background: var(--page-bg);
    font-family: "Open Sans", Arial, sans-serif;
  }
  .canvas { position: relative; width: 1200px; height: 864px; }

  .card {
    position: absolute;
    width: 540px; height: 309px;
    background: var(--card-bg);
    border: 1px solid var(--card-edge);
    border-radius: 3px;
    box-shadow: 0 10px 24px rgba(0,0,0,.16);
    overflow: hidden;
  }
  .card--back { left: 50px; top: 100px; }
  .card--front { left: 610px; top: 455px; }

  /* Back side */
  .back-brand {
    position: absolute; left: 0; right: 0; top: 104px;
    display: flex; justify-content: center; align-items: center; gap: 14px;
  }
  .brand-square { width: 22px; height: 22px; background: var(--brand-blue); }
  .back-brand .brand-name {
    font-size: 38px; font-weight: 700; color: var(--brand-blue); letter-spacing: 1px;
  }
  .back-web {
    position: absolute; left: 0; right: 0; top: 200px; text-align: center;
    font-size: 13px; letter-spacing: 5px; color: var(--text-muted);
  }

  /* Front side */
  .front-brand {
    position: absolute; right: 30px; top: 50px; text-align: right;
  }
  .front-brand .brand-name {
    font-size: 28px; font-weight: 700; color: var(--brand-blue); letter-spacing: .5px;
    line-height: 1;
  }
  .brand-rule {
    height: 2px; background: var(--brand-blue); margin-top: 10px; width: 250px; margin-left: auto;
  }

  .person { position: absolute; left: 34px; top: 116px; }
  .person-name {
    font-size: 18px; font-weight: 700; color: var(--brand-blue); text-transform: uppercase; line-height: 1.1;
  }
  .person-title {
    font-size: 12px; color: var(--text-muted); text-transform: uppercase; letter-spacing: .5px; margin-top: 2px;
  }

  .divider {
    position: absolute; left: 34px; top: 170px; width: 472px; height: 1px; background: var(--rule);
  }

  .contact-list { position: absolute; left: 34px; top: 182px; list-style: none; }
  .contact-list li {
    display: flex; align-items: center; gap: 9px;
    font-size: 13px; color: var(--text-dark); line-height: 21px;
  }
  .contact-list svg { width: 12px; height: 12px; fill: var(--brand-blue); flex: none; }

  .address {
    position: absolute; right: 30px; bottom: 26px; text-align: right;
    font-size: 14px; color: var(--text-dark); line-height: 20px; font-style: normal;
  }
</style>
</head>
<body>
<main class="canvas">

  <section class="card card--back" aria-label="Business card back">
    <div class="back-brand">
      <span class="brand-square"></span>
      <span class="brand-name">BOLT REMOVE</span>
    </div>
    <p class="back-web">www.boltremove.co.uk</p>
  </section>

  <section class="card card--front" aria-label="Business card front">
    <div class="front-brand">
      <p class="brand-name">BOLT REMOVE LTD</p>
      <div class="brand-rule"></div>
    </div>

    <div class="person">
      <h1 class="person-name">Daniel Hartley</h1>
      <p class="person-title">General Manager</p>
    </div>

    <div class="divider"></div>

    <ul class="contact-list">
      <li>
        <svg viewBox="0 0 24 24" aria-hidden="true"><path d="M6.6 10.8a15.1 15.1 0 0 0 6.6 6.6l2.2-2.2c.3-.3.7-.4 1-.2 1.1.4 2.3.6 3.6.6.6 0 1 .4 1 1V20c0 .6-.4 1-1 1A17 17 0 0 1 3 4c0-.6.4-1 1-1h3.5c.6 0 1 .4 1 1 0 1.3.2 2.5.6 3.6.1.3 0 .7-.2 1l-2.3 2.2z"/></svg>
        0161 555 0142
      </li>
      <li>
        <svg viewBox="0 0 24 24" aria-hidden="true"><path d="M7 1h10a2 2 0 0 1 2 2v18a2 2 0 0 1-2 2H7a2 2 0 0 1-2-2V3a2 2 0 0 1 2-2zm0 3v14h10V4H7zm5 15.5a1 1 0 1 0 0 2 1 1 0 0 0 0-2z"/></svg>
        07700 900 318
      </li>
      <li>
        <svg viewBox="0 0 24 24" aria-hidden="true"><path d="M2 5h20v14H2V5zm2 2v.4l8 5 8-5V7H4zm16 2.8-8 5-8-5V17h16V9.8z"/></svg>
        dhartley@boltremove.co.uk
      </li>
      <li>
        <svg viewBox="0 0 24 24" aria-hidden="true"><path d="M12 2a10 10 0 1 0 0 20 10 10 0 0 0 0-20zm6.9 6h-3a15.7 15.7 0 0 0-1.3-3.6A8 8 0 0 1 18.9 8zM12 4c.8 1.2 1.5 2.5 1.9 4h-3.8c.4-1.5 1.1-2.8 1.9-4zM4.3 14a8.2 8.2 0 0 1 0-4h3.4a16 16 0 0 0 0 4H4.3zm.8 2h3a15.7 15.7 0 0 0 1.3 3.6A8 8 0 0 1 5.1 16zm3-8h-3a8 8 0 0 1 4.3-3.6C8.8 5.6 8.4 6.8 8.1 8zM12 20c-.8-1.2-1.5-2.5-1.9-4h3.8c-.4 1.5-1.1 2.8-1.9 4zm2.3-6H9.7a14.7 14.7 0 0 1 0-4h4.6a14.7 14.7 0 0 1 0 4zm.3 5.6c.6-1.1 1-2.3 1.3-3.6h3a8 8 0 0 1-4.3 3.6zm1.7-5.6a16 16 0 0 0 0-4h3.4a8.2 8.2 0 0 1 0 4h-3.4z"/></svg>
        www.boltremove.co.uk
      </li>
    </ul>

    <address class="address">
      Mill Lane<br>
      Northfield, Eastport<br>
      NP4 7QD
    </address>
  </section>

</main>
</body>
</html>
```